A hand soap seller needs a premium label for a new product

We need a premium label for a bottle of soap. We want to write on it:
TAVRELMIK (Name)
Hypoallergenic and antibacterial hand soap
350 ml e / 11.8 fl oz (volume, http://pramvel.ru/7Q2KsNbwTre845)
Saint Petersburg - Russia / www.tavrelmik.ru
We want to see the face of a hippopotamus in the design. Use only black and white and green for accents (the color of grass). Examples of a hippopotamus are shown in the photo. Our soap is hypoallergenic. Ideal for both children and adults. Therefore, the label should appeal to adults and children.
The bottle will be white, and the soap dispenser will be black.
So I'm attaching an example of a soap design that we liked
Label size: height-78 mm, width-102 mm !!!

Target Market(s)

Mothers and children

Industry/Entity Type

Hand soap

Font styles to use
Serif

Colors

Designer to choose only greyscale colors for use in the design.

Requirements
Must have
• The face of a hippopotamus emerging from the grass, Black and white palette with elements of green (grass color)
Nice to have
• The face of a hippopotamus emerging from the grass
Should not have
• Different colors

```html
<!DOCTYPE html>
<html lang="en">
<head>
<meta charset="utf-8">
<title>TAVRELMIK — Hand Soap Label</title>
<link rel="stylesheet" href="https://fonts.googleapis.com/css2?family=Roboto+Condensed:wght@300;700&display=swap">
<style>
  :root {
    --paper: #e8e8ea;
    --ink: #2f2e30;
    --night: #333233;
    --snow: #f2f2f2;
    --art-light: #b9b9bc;
    --art-dark: #5a595b;
  }
  * { margin: 0; padding: 0; box-sizing: border-box; }
  html, body { width: 1200px; height: 1000px; overflow: hidden; }
  body {
    display: flex;
    font-family: "Roboto Condensed", "Arial Narrow", sans-serif;
  }
  .label {
    width: 600px;
    height: 1000px;
    display: flex;
    flex-direction: column;
    align-items: center;
    padding-top: 200px;
    text-align: center;
  }
  .label--light { background: var(--paper); color: var(--ink); }
  .label--dark { background: var(--night); color: var(--snow); }
  .hippo-art {
    width: 230px;
    height: 220px;
    border-radius: 110px 110px 20px 20px;
  }
  .label--light .hippo-art { background: linear-gradient(180deg, var(--art-light), #a4a4a8); }
  .label--dark .hippo-art { background: linear-gradient(180deg, var(--art-dark), #6a696b); }
  .brand-name {
    margin-top: 22px;
    font-size: 62px;
    font-weight: 700;
    letter-spacing: 3px;
    line-height: 1;
  }
  .product-type {
    margin-top: 14px;
    font-size: 23px;
    font-weight: 700;
    line-height: 1.2;
  }
  .origin {
    margin-top: 80px;
    font-size: 22px;
    font-weight: 300;
    line-height: 1.3;
  }
  .volume {
    margin-top: 26px;
    font-size: 30px;
    font-weight: 700;
  }
</style>
</head>
<body>
  <section class="label label--light">
    <div class="hippo-art" role="img" aria-label="Line illustration of a hippopotamus head emerging from grass"></div>
    <h1 class="brand-name">TAVRELMIK</h1>
    <p class="product-type">Hypoallergenic<br>And<br>Antibacterial Hand Soap</p>
    <p class="origin">Saint Petersburg - Russia<br>www.tavrelmik.ru</p>
    <p class="volume">350 ml e / 11.8 fl oz</p>
  </section>
  <section class="label label--dark">
    <div class="hippo-art" role="img" aria-label="Light line illustration of a hippopotamus head emerging from grass"></div>
    <h1 class="brand-name">TAVRELMIK</h1>
    <p class="product-type">Hypoallergenic<br>And<br>Antibacterial Hand Soap</p>
    <p class="origin">Saint Petersburg - Russia<br>www.tavrelmik.ru</p>
    <p class="volume">350 ml e / 11.8 fl oz</p>
  </section>
</body>
</html>
```